An animal window cleaning business card

I want a business card design that includes a logo and tells people I am a WINDOW WASHING COMPANY right away.
Were based in Maine, we do window cleaning, pressure washing, and gutter cleaning. We like Pine trees, the Ocean, state of Maine symbols, Lobsters, Moose, Huskies, etc. My business name is "BRIGHT PANE WINDOWS"
The card could also be designed to look like a gift credit card with a 50$ value.

Target Market(s)

my target audience is older folks with disposable money who live on the ocean or have secondary homes for vacation in Maine

Industry/Entity Type

Cleaning Services

Contact Information for Business Card

2.5x3" plastic if possible.

Font styles to use
Sans Serif

Requirements
Must have
• a symbol, or a logo that tells people I am a window washing company Instantly.
The words BRIGHT PANE, my phone number, my name, MY email
Nice to have
• a lobster holding a squeegee, or a stylized cartoonish version of a human huskie holding a squeegee,
Should not have
• a lighthouse
small hard to read text

```html
<!DOCTYPE html>
<html lang="en">
<head>
<meta charset="UTF-8">
<title>Bright Pane Windows – Business Card</title>
<link href="https://fonts.googleapis.com/css2?family=Nunito+Sans:wght@800&family=Arimo:wght@400&display=swap" rel="stylesheet">
<style>
  :root {
    --navy: #1b1464;
    --green: #9bcb3c;
    --white: #ffffff;
    --backdrop: #747474;
  }
  * { margin: 0; padding: 0; box-sizing: border-box; }
  html, body {
    width: 1200px; height: 801px; overflow: hidden;
    background: var(--backdrop);
  }
  .card {
    position: absolute;
    width: 442px; height: 261px;
    border-radius: 18px;
    overflow: hidden;
  }
  .card-front { left: 155px; top: 274px; background: var(--navy); }
  .card-back { left: 625px; top: 275px; background: var(--white); }

  .brand {
    position: absolute;
    display: flex; flex-direction: column; align-items: center;
  }
  .brand-mark { width: 26px; height: 26px; background: var(--green); margin-bottom: 14px; }
  .brand-name {
    font-family: "Nunito Sans", sans-serif;
    font-weight: 800;
    white-space: nowrap;
    letter-spacing: -0.2px;
  }
  .card-front .brand { left: 25px; top: 52px; width: 240px; }
  .card-front .brand-name { color: var(--white); font-size: 19px; }
  .card-back .brand { left: 0; right: 0; top: 68px; }
  .card-back .brand-name { color: var(--navy); font-size: 21px; }
  .card-back .brand-mark { width: 30px; height: 30px; margin-bottom: 24px; }

  .gift-value {
    position: absolute; right: 26px; top: 38px;
    font-family: "Arimo", sans-serif;
    font-size: 29px; color: var(--green);
  }
  .holder { position: absolute; left: 25px; top: 196px; }
  .holder-name {
    font-family: "Nunito Sans", sans-serif; font-weight: 800;
    font-size: 19px; color: var(--green); line-height: 22px;
  }
  .holder-role {
    font-family: "Arimo", sans-serif;
    font-size: 16px; color: var(--white); line-height: 20px;
  }
  .contacts {
    position: absolute; right: 22px; top: 178px;
    list-style: none;
    font-family: "Arimo", sans-serif;
    font-size: 16px; color: var(--white);
  }
  .contacts li {
    display: flex; align-items: center; justify-content: flex-end;
    gap: 5px; height: 19.5px;
  }
  .contacts svg { width: 13px; height: 13px; fill: none; stroke: var(--green); stroke-width: 2; }

  .services {
    position: absolute; left: 0; right: 0; top: 184px; height: 44px;
    background: var(--navy);
    display: flex; align-items: center; justify-content: center; gap: 2px;
    font-family: "Arimo", sans-serif;
    font-size: 15px; color: var(--white);
  }
  .services svg { width: 13px; height: 13px; fill: var(--green); }
</style>
</head>
<body>
  <section class="card card-front">
    <div class="brand">
      <span class="brand-mark"></span>
      <span class="brand-name">BRIGHT PANE WINDOWS</span>
    </div>
    <div class="gift-value">$50</div>
    <div class="holder">
      <div class="holder-name">DANIEL HARTLEY</div>
      <div class="holder-role">Managing Director</div>
    </div>
    <ul class="contacts">
      <li>207-555 014 326
        <svg viewBox="0 0 24 24"><path d="M5 3l4 1 1 5-2 2a12 12 0 0 0 5 5l2-2 5 1 1 4-3 2C10 21 3 14 2 6z"/></svg></li>
      <li>hello@brightpane.com
        <svg viewBox="0 0 24 24"><rect x="2" y="5" width="20" height="14"/><path d="M2 5l10 8 10-8"/></svg></li>
      <li>www.brightpane.com
        <svg viewBox="0 0 24 24"><circle cx="12" cy="12" r="10"/><path d="M2 12h20M12 2c-5 6-5 14 0 20M12 2c5 6 5 14 0 20"/></svg></li>
    </ul>
  </section>

  <section class="card card-back">
    <div class="brand">
      <span class="brand-mark"></span>
      <span class="brand-name">BRIGHT PANE WINDOWS</span>
    </div>
    <div class="services">
      <span>Window Cleaning</span>
      <svg viewBox="0 0 24 24"><path d="M12 0l3 9 9 3-9 3-3 9-3-9-9-3 9-3z"/></svg>
      <span>Pressure Washing</span>
      <svg viewBox="0 0 24 24"><path d="M12 0l3 9 9 3-9 3-3 9-3-9-9-3 9-3z"/></svg>
      <span>Gutter Cleaning</span>
    </div>
  </section>
</body>
</html>
```